Format / Design slides - NEED ASAP!!!

Format ONLY slides 4 - 11 and and slide 16.
Make look like slides 12 and 13.

Do NOT worry about slides after the Appendix.
Does not have to look super fancy, just better than what I have.

```html
<!DOCTYPE html>
<html lang="en">
<head>
<meta charset="utf-8">
<title>Hypothetical Case Study</title>
<link rel="stylesheet" href="https://fonts.googleapis.com/css2?family=Libre+Franklin:wght@400;500;600;700&display=swap">
<style>
  :root {
    --navy: #0c2d74;
    --title-blue: #1d3c95;
    --highlight: #ffff00;
    --band: #d9f1d3;
    --band-text: #3f8a2f;
    --ink: #222222;
    --rule: #9a9a9a;
    --accent: #7fbfe8;
    --page-num: #3b86d6;
  }
  * { margin: 0; padding: 0; box-sizing: border-box; }
  html, body { width: 1200px; height: 873px; overflow: hidden; background: #ffffff; }
  body { font-family: "Libre Franklin", Arial, sans-serif; color: var(--ink); }
  .slide { position: relative; width: 1200px; height: 873px; }

  .slide-title {
    position: absolute; left: 25px; top: 48px; height: 32px;
    padding: 0 6px; background: var(--highlight);
    color: var(--title-blue); font-size: 20px; font-weight: 500;
    line-height: 32px; letter-spacing: 0.2px;
  }
  .title-rule { position: absolute; left: 25px; top: 83px; width: 1148px; height: 1px; background: var(--rule); }

  .brand {
    position: absolute; right: 14px; top: 28px;
    display: flex; align-items: center; gap: 8px;
  }
  .brand-mark { width: 26px; height: 26px; background: var(--accent); }
  .brand-name { font-size: 16px; font-weight: 700; color: var(--navy); }

  .intro {
    position: absolute; left: 46px; top: 108px; width: 1110px;
    font-size: 15.5px; line-height: 24px; color: #1a1a1a;
  }
  .table-caption {
    position: absolute; left: 46px; top: 185px;
    font-size: 13px; font-weight: 600; color: var(--band-text); letter-spacing: -0.2px;
  }

  .case-table {
    position: absolute; left: 37px; top: 213px; width: 1126px;
    border-collapse: collapse; table-layout: fixed; font-size: 13.5px;
  }
  .case-table col.label { width: 213px; }
  .case-table col.c1 { width: 234px; }
  .case-table col.c2 { width: 230px; }
  .case-table col.c3 { width: 220px; }
  .case-table col.c4 { width: 229px; }
  .case-table td { height: 38px; text-align: center; vertical-align: middle; }
  .case-table td:first-child { text-align: left; padding-left: 11px; }
  .case-table tr.band td { background: var(--band); color: var(--band-text); font-weight: 600; letter-spacing: -0.3px; }
  .case-table tr.head td { height: 35px; }
  .case-table tr.tall td { height: 50px; line-height: 18px; }

  .footer { position: absolute; left: 0; top: 841px; width: 1200px; height: 32px; }
  .footer svg { position: absolute; left: 0; top: 0; }
  .footer-label {
    position: absolute; top: 0; line-height: 32px;
    font-size: 11px; color: #ffffff; letter-spacing: 0.2px;
  }
  .footer-left { left: 44px; }
  .footer-date { left: 1011px; }
  .page-number {
    position: absolute; right: 14px; top: 0; line-height: 32px;
    font-size: 13px; color: var(--page-num);
  }
</style>
</head>
<body>
<main class="slide">
  <h1 class="slide-title">HYPOTHETICAL CASE STUDY ????</h1>
  <div class="title-rule"></div>

  <div class="brand">
    <span class="brand-mark"></span>
    <span class="brand-name">Northcrest REIT</span>
  </div>

  <p class="intro">For top-tier, high-occupancy assets, REVPOR is materially outpacing EXPOR, widening operating spreads. A ~200 bp rate-over-expense delta supports durable high-single-digit to low-double-digit NOI growth with no reliance on occupancy lift.</p>

  <p class="table-caption">Hypothetical AL Asset Stabilized at 95% Occupancy / 30% Margin</p>

  <table class="case-table">
    <colgroup><col class="label"><col class="c1"><col class="c2"><col class="c3"><col class="c4"></colgroup>
    <tbody>
      <tr class="band head"><td>Occupancy Change (%)</td><td></td><td>0.0%</td><td>0.25%</td><td>0.5%</td></tr>
      <tr><td>Units</td><td>85</td><td>85</td><td>85</td><td>85</td></tr>
      <tr><td>Occupancy</td><td>95.0%</td><td>95.0%</td><td>95.3%</td><td>95.5%</td></tr>
      <tr><td>Occupied Units</td><td>80.75</td><td>80.75</td><td>80.9625</td><td>81.175</td></tr>
      <tr><td>REVPOR</td><td>8,000</td><td>8,400</td><td>8,400</td><td>8,400</td></tr>
      <tr><td>Base REVPOR Growth</td><td>5%</td><td>5.0%</td><td>5.0%</td><td>5.0%</td></tr>
      <tr><td>EXPOR</td><td>5,600</td><td>5,768</td><td>5,764</td><td>5,760</td></tr>
      <tr><td>Base EXPOR Growth</td><td>3%</td><td>3.00%</td><td>2.93%</td><td>2.85%</td></tr>
      <tr><td>Margin</td><td>30.0%</td><td>31.3%</td><td>31.4%</td><td>31.4%</td></tr>
      <tr><td>Revenues</td><td>7,752,000</td><td>8,139,600</td><td>8,161,020</td><td>8,182,440</td></tr>
      <tr><td>Expenses</td><td>5,426,400</td><td>5,589,192</td><td>5,599,820</td><td>5,610,426</td></tr>
      <tr><td>NOI</td><td>2,325,600</td><td>2,550,408</td><td>2,561,200</td><td>2,572,014</td></tr>
      <tr class="band"><td>NOI GR</td><td></td><td>9.7%</td><td>10.1%</td><td>10.6%</td></tr>
      <tr><td>Revenue Growth</td><td></td><td>5.00%</td><td>5.28%</td><td>5.55%</td></tr>
      <tr><td>Expense Growth</td><td></td><td>3.00%</td><td>3.20%</td><td>3.39%</td></tr>
      <tr class="tall"><td>Incremental Margin On<br>Revenue Increase</td><td></td><td>58.0%</td><td>57.6%</td><td>57.2%</td></tr>
    </tbody>
  </table>

  <footer class="footer">
    <svg width="1200" height="32" aria-hidden="true">
      <polygon points="0,0 1152,0 1165,16 1152,32 0,32" fill="var(--navy)"/>
    </svg>
    <span class="footer-label footer-left">INVESTOR PRESENTATION</span>
    <span class="footer-label footer-date">MARCH 2026</span>
    <span class="page-number">16</span>
  </footer>
</main>
</body>
</html>
```